Aesthetics Company Flyer (description of services)

We need a 5.5"x8.5" flyer describing the services we offer at radiant meadowbrook aesthetics. We are an aesthetics company located in Conroe TX. Our products and services can be found at www.rmaesthetica.example/services . We would like to see designs that are cohesive with our brand and website: https://www.rmaesthetica.example/

```html
<!DOCTYPE html>
<html lang="en">
<head>
<meta charset="utf-8">
<title>Radiant Meadowbrook Aesthetics – Services Flyer</title>
<link rel="stylesheet" href="https://fonts.googleapis.com/css2?family=Barlow:wght@500;600&family=Poppins:ital,wght@0,400;0,500;0,600;0,700;1,500&display=swap">
<style>
  :root {
    --lilac: #ccb4f4;
    --lilac-deep: #a98ae9;
    --ink: #1c1a1f;
    --paper: #ffffff;
    --hatch: #d6d2dc;
    --photo-dark: #2e2c2d;
    --photo-warm: #d9b69c;
    --photo-light: #ece7ea;
  }
  * { margin: 0; padding: 0; box-sizing: border-box; }
  html, body { width: 776px; height: 1200px; overflow: hidden; background: var(--paper); }
  .flyer { position: relative; width: 776px; height: 1200px; background: var(--paper); color: var(--ink); font-family: "Poppins", sans-serif; overflow: hidden; }
  .abs { position: absolute; }

  .hero-band { left: 0; top: 0; width: 776px; height: 260px; background: var(--lilac); }
  .hero-band-tail { left: 376px; top: 259px; width: 400px; height: 24px; background: var(--lilac); }
  .brand-badge { left: 607px; top: -14px; width: 170px; height: 166px; border-radius: 50%; background: var(--paper); display: flex; align-items: center; justify-content: center; text-align: center; }
  .brand-badge span { font-weight: 500; font-size: 10px; letter-spacing: 1.5px; line-height: 1.5; text-transform: uppercase; width: 110px; margin-top: 20px; }

  .title { left: 72px; top: 44px; font-family: "Barlow", sans-serif; font-weight: 600; font-size: 66px; line-height: 64px; letter-spacing: 1px; }
  .tagline { left: 76px; top: 184px; font-size: 21px; line-height: 28px; letter-spacing: 3px; text-transform: uppercase; }
  .tagline em { font-style: italic; font-weight: 500; }

  .stripes { background: var(--hatch); }
  .stripes-top { left: 529px; top: 267px; width: 247px; height: 33px; }
  .stripes-low { left: 376px; top: 512px; width: 153px; height: 43px; }

  .photo-hero { left: 0; top: 284px; width: 351px; height: 307px; background: linear-gradient(100deg, var(--photo-warm) 0%, #e9d2c3 45%, var(--photo-dark) 80%); }

  .mission { right: 45px; top: 328px; text-align: right; font-weight: 700; font-size: 21px; line-height: 28px; }
  .mission .accent { color: var(--lilac-deep); }

  .about-box { left: 376px; top: 400px; width: 400px; height: 133px; background: var(--lilac); }
  .about-text { right: 45px; top: 422px; width: 320px; text-align: right; font-size: 15px; line-height: 19px; }

  .frame-back { left: 534px; top: 571px; width: 211px; height: 247px; background: var(--lilac); }
  .photo-treatment { left: 514px; top: 591px; width: 210px; height: 247px; background: linear-gradient(135deg, #f3c6e6 0%, var(--photo-light) 45%, #e8d3c6 100%); }

  .iv-band { left: 0; top: 616px; width: 264px; height: 47px; background: var(--lilac); }
  .iv-tab { left: 280px; top: 616px; width: 12px; height: 47px; background: var(--lilac); }
  .iv-title { left: 57px; top: 627px; font-weight: 700; font-size: 22px; line-height: 26px; }

  .iv-list { list-style: none; font-size: 15px; line-height: 31px; }
  .iv-list li { display: flex; align-items: center; gap: 10px; height: 31px; }
  .iv-list svg { flex: none; }
  .iv-col-a { left: 54px; top: 679px; }
  .iv-col-b { left: 278px; top: 679px; }

  .services-band { left: 0; top: 866px; width: 776px; height: 178px; background: var(--lilac); }
  .service { top: 884px; width: 112px; text-align: center; }
  .service .thumb { width: 100px; height: 109px; margin: 0 auto; }
  .service .label { margin-top: 10px; font-weight: 600; font-size: 13.5px; line-height: 17px; }

  .book { left: 57px; top: 1062px; font-family: "Barlow", sans-serif; font-weight: 600; font-size: 35px; line-height: 35px; text-align: right; }
  .spark { left: 37px; top: 1094px; }

  .contacts { left: 187px; top: 1058px; list-style: none; font-size: 14px; }
  .contacts li { display: flex; align-items: center; gap: 10px; height: 27px; }

  .divider { left: 431px; top: 1057px; width: 1px; height: 81px; background: var(--ink); }
  .hours-title { left: 471px; top: 1058px; font-family: "Barlow", sans-serif; font-weight: 600; font-size: 20px; line-height: 24px; }
  .hours { font-size: 13px; line-height: 16.5px; }
  .hours .day { color: var(--lilac-deep); font-weight: 600; display: inline-block; width: 22px; }
  .hours-a { left: 471px; top: 1089px; }
  .hours-b { left: 588px; top: 1089px; }

  .address-band { left: 0; top: 1150px; width: 776px; height: 50px; background: var(--lilac); display: flex; align-items: center; justify-content: center; gap: 8px; font-weight: 500; font-size: 14px; }
</style>
</head>
<body>
<main class="flyer">
  <div class="abs hero-band"></div>
  <div class="abs hero-band-tail"></div>
  <div class="abs brand-badge"><span>Radiant Meadowbrook Aesthetics</span></div>

  <h1 class="abs title">RADIANT<br>MEADOWBROOK</h1>
  <p class="abs tagline">Everyone is beautiful.<br>With us, <em>everyone can feel beautiful too</em></p>

  <div class="abs stripes stripes-top" role="img" aria-label="Diagonal hatch stripe accent"></div>
  <div class="abs photo-hero" role="img" aria-label="Portrait photo of two smiling women with glowing skin"></div>

  <h2 class="abs mission">WE CHANGE THE WORLD<br>ONE <span class="accent">BEAUTIFUL FACE</span> AT A TIME</h2>

  <div class="abs about-box"></div>
  <p class="abs about-text">At Radiant Meadowbrook Aesthetics we offer a comprehensive list of aesthetic, skincare and weight loss services and<br>IV hydration therapy.</p>
  <div class="abs stripes stripes-low" role="img" aria-label="Diagonal hatch stripe accent"></div>

  <div class="abs frame-back"></div>
  <div class="abs photo-treatment" role="img" aria-label="Photo of a facial treatment with gloved hands and a roller tool"></div>

  <div class="abs iv-band"></div>
  <div class="abs iv-tab"></div>
  <h2 class="abs iv-title">IV HYDRATION</h2>

  <ul class="abs iv-list iv-col-a">
    <li><svg width="17" height="17" viewBox="0 0 17 17"><circle cx="8.5" cy="8.5" r="8.5" fill="#ccb4f4"/><path d="M3.5 8.5l3.5 3.5 8-8.5" fill="none" stroke="#1c1a1f" stroke-width="1.8"/></svg>Quench Hydrator</li>
    <li><svg width="17" height="17" viewBox="0 0 17 17"><circle cx="8.5" cy="8.5" r="8.5" fill="#ccb4f4"/><path d="M3.5 8.5l3.5 3.5 8-8.5" fill="none" stroke="#1c1a1f" stroke-width="1.8"/></svg>Glutathione</li>
    <li><svg width="17" height="17" viewBox="0 0 17 17"><circle cx="8.5" cy="8.5" r="8.5" fill="#ccb4f4"/><path d="M3.5 8.5l3.5 3.5 8-8.5" fill="none" stroke="#1c1a1f" stroke-width="1.8"/></svg>Vitality Cocktail</li>
    <li><svg width="17" height="17" viewBox="0 0 17 17"><circle cx="8.5" cy="8.5" r="8.5" fill="#ccb4f4"/><path d="M3.5 8.5l3.5 3.5 8-8.5" fill="none" stroke="#1c1a1f" stroke-width="1.8"/></svg>Hangover</li>
    <li><svg width="17" height="17" viewBox="0 0 17 17"><circle cx="8.5" cy="8.5" r="8.5" fill="#ccb4f4"/><path d="M3.5 8.5l3.5 3.5 8-8.5" fill="none" stroke="#1c1a1f" stroke-width="1.8"/></svg>Post Workout Recovery</li>
  </ul>
  <ul class="abs iv-list iv-col-b">
    <li><svg width="17" height="17" viewBox="0 0 17 17"><circle cx="8.5" cy="8.5" r="8.5" fill="#ccb4f4"/><path d="M3.5 8.5l3.5 3.5 8-8.5" fill="none" stroke="#1c1a1f" stroke-width="1.8"/></svg>Migraine Rescue</li>
    <li><svg width="17" height="17" viewBox="0 0 17 17"><circle cx="8.5" cy="8.5" r="8.5" fill="#ccb4f4"/><path d="M3.5 8.5l3.5 3.5 8-8.5" fill="none" stroke="#1c1a1f" stroke-width="1.8"/></svg>Immunity Booster</li>
    <li><svg width="17" height="17" viewBox="0 0 17 17"><circle cx="8.5" cy="8.5" r="8.5" fill="#ccb4f4"/><path d="M3.5 8.5l3.5 3.5 8-8.5" fill="none" stroke="#1c1a1f" stroke-width="1.8"/></svg>Radiant Glow</li>
    <li><svg width="17" height="17" viewBox="0 0 17 17"><circle cx="8.5" cy="8.5" r="8.5" fill="#ccb4f4"/><path d="M3.5 8.5l3.5 3.5 8-8.5" fill="none" stroke="#1c1a1f" stroke-width="1.8"/></svg>Peak Athletic Performance</li>
    <li><svg width="17" height="17" viewBox="0 0 17 17"><circle cx="8.5" cy="8.5" r="8.5" fill="#ccb4f4"/><path d="M3.5 8.5l3.5 3.5 8-8.5" fill="none" stroke="#1c1a1f" stroke-width="1.8"/></svg>NAD+</li>
  </ul>

  <div class="abs services-band"></div>
  <div class="abs service" style="left:51px"><div class="thumb" role="img" aria-label="Photo of a weight loss injection pen" style="background:linear-gradient(135deg,#c9773f,#eec8a4)"></div><p class="label">Weightloss</p></div>
  <div class="abs service" style="left:163px"><div class="thumb" role="img" aria-label="Photo of a neurotoxin injection treatment" style="background:linear-gradient(135deg,#f2eeee,#6b4a3a)"></div><p class="label">Neurotoxin</p></div>
  <div class="abs service" style="left:276px"><div class="thumb" role="img" aria-label="Photo of a dermal filler treatment" style="background:linear-gradient(135deg,#d9a58b,#3fb5dc)"></div><p class="label">Dermal Fillers</p></div>
  <div class="abs service" style="left:388px"><div class="thumb" role="img" aria-label="Photo of a growth factor facial treatment" style="background:linear-gradient(135deg,#f4f1f1,#d6ad98)"></div><p class="label">Fibrin Growth<br>Factor</p></div>
  <div class="abs service" style="left:500px"><div class="thumb" role="img" aria-label="Photo of a microneedling pen treatment" style="background:linear-gradient(135deg,#e8cdb8,#f6ece6)"></div><p class="label">VelvetGlide</p></div>
  <div class="abs service" style="left:613px"><div class="thumb" role="img" aria-label="Photo of a chemical peel application" style="background:linear-gradient(135deg,#e7c93a,#f2f0f0)"></div><p class="label">Chemical<br>Peels</p></div>

  <p class="abs book">BOOK<br>NOW</p>
  <svg class="abs spark" width="26" height="26" viewBox="0 0 26 26" aria-hidden="true"><path d="M13 0C14 9 17 12 26 13C17 14 14 17 13 26C12 17 9 14 0 13C9 12 12 9 13 0Z" fill="#ccb4f4"/></svg>

  <ul class="abs contacts">
    <li><svg width="16" height="16" viewBox="0 0 24 24"><path d="M6.6 10.8a15 15 0 0 0 6.6 6.6l2.2-2.2c.3-.3.7-.4 1-.2 1.1.4 2.3.6 3.6.6.6 0 1 .4 1 1V20c0 .6-.4 1-1 1A17 17 0 0 1 3 4c0-.6.4-1 1-1h3.5c.6 0 1 .4 1 1 0 1.3.2 2.5.6 3.6.1.3 0 .7-.2 1z" fill="#1c1a1f"/></svg>936 555 0142</li>
    <li><svg width="16" height="12" viewBox="0 0 16 12"><rect x="0.5" y="0.5" width="15" height="11" fill="#1c1a1f"/><path d="M1 1l7 6 7-6M1 11l5-4.5M15 11l-5-4.5" fill="none" stroke="#fff" stroke-width="1.2"/></svg>hello@rmaesthetica.example</li>
    <li><svg width="16" height="16" viewBox="0 0 16 16"><circle cx="8" cy="8" r="7" fill="none" stroke="#1c1a1f" stroke-width="1.5"/><ellipse cx="8" cy="8" rx="3" ry="7" fill="none" stroke="#1c1a1f" stroke-width="1.5"/><path d="M1 8h14" stroke="#1c1a1f" stroke-width="1.5"/></svg>rmaesthetica.example</li>
  </ul>

  <div class="abs divider"></div>
  <h2 class="abs hours-title">OPENING HOURS</h2>
  <p class="abs hours hours-a"><span class="day">M</span>9:00 - 6:30<br><span class="day">Tu</span>8:30 - 3:30<br><span class="day">W</span>8:30 - 6:30</p>
  <p class="abs hours hours-b"><span class="day">Th</span>8:30 - 3:30<br><span class="day">F</span>8:30 - 2:30</p>

  <div class="abs address-band">
    <svg width="16" height="20" viewBox="0 0 16 20"><path d="M8 0a8 8 0 0 0-8 8c0 6 8 12 8 12s8-6 8-12a8 8 0 0 0-8-8z" fill="#1c1a1f"/><circle cx="8" cy="8" r="3" fill="#ccb4f4"/></svg>
    <span>2710 Meadow Ridge Rd #140 Willowbend, TX 77390 &nbsp;(Across from Lakeside Cinema)</span>
  </div>
</main>
</body>
</html>
```